Venlox - Property Management Company Listings - PSD / uncoded only

Our site simply connects property owners with property managers. I’m asking you to create 2 pages, 1 homepage and 1 page that lists of property management companies. Build with Responsive Design in mind. PSD/uncoded files only. Help us create a great site!
Example competitor sites:
http://www.everyestatehelp.example/
http://www.tendyourlots.example/
Inspired by these sites:
http://www.quorvik.example/
http://www.bespokely.example/
http://www.coinwire.example/
https://www.tripboard.example/
I've attached the logo as well as 2 picture files that you can consider using.
• Venlox Logo Colors: Yellow: HTML code: #FBC30A, RGB code: R: 251 G: 195 B: 10 Grey: HTML code: #4E4C4D, RGB code: R: 78 G: 76 B: 77
• The picture files are optional.
o One picture is of houses and neighborhood.
o The other is of a professional woman on the phone. Please do not use the professional woman as a large primary image. You can use the professional woman photo as a smaller photo and not the main photo.
• Please bring your own pictures and graphics too. Don't feel like you need to use mine.
Thank you!

```html
<!DOCTYPE html>
<html lang="en">
<head>
<meta charset="utf-8">
<title>Venlox – Find Your Local Property Manager</title>
<link href="https://fonts.googleapis.com/css2?family=Lato:ital,wght@0,300;0,400;0,700;1,300&display=swap" rel="stylesheet">
<style>
:root{
  --yellow:#fbc30a;
  --grey:#4e4c4d;
  --text:#444;
  --panel:#f0f0f0;
  --dark:#333;
}
*{box-sizing:border-box;margin:0;padding:0}
html,body{width:1200px;height:1156px;overflow:hidden}
body{font-family:'Lato',sans-serif;color:var(--text);background:#fff;position:relative}
.abs{position:absolute}

.site-header{position:absolute;left:0;top:0;width:1200px;height:110px;background:#fff;border-bottom:3px solid var(--yellow)}
.brand{position:absolute;left:36px;top:30px;display:flex;align-items:center;gap:10px}
.brand-mark{width:22px;height:22px;background:var(--yellow)}
.brand-name{font-size:58px;font-weight:700;color:var(--grey);line-height:1;letter-spacing:-1px}
.topbar{position:absolute;right:34px;top:5px;font-size:14px;color:var(--grey);display:flex;align-items:center;gap:12px}
.main-nav{position:absolute;top:46px;right:37px;display:flex;gap:58px}
.nav-item{display:flex;flex-direction:column;align-items:center;gap:5px;font-size:17px;font-weight:700;color:var(--grey)}
.nav-item svg{width:18px;height:20px;fill:var(--grey)}

.hero{position:absolute;left:0;top:110px;width:1200px;height:400px;background:linear-gradient(180deg,#b8b2ac 0%,#c9b9ab 35%,#a7846f 70%,#7b6c5e 100%)}
.search-panel{position:absolute;left:227px;top:133px;width:747px;height:217px;background:rgba(251,195,10,.93);text-align:center}
.search-panel h1{margin-top:21px;font-size:25px;font-weight:700;color:var(--grey);letter-spacing:-.3px}
.field-label{position:absolute;top:76px;font-size:14px;color:var(--grey)}
.select-box{position:absolute;left:31px;top:100px;width:386px;height:36px;background:#fff;border:1px solid #ccc;font-size:15px;color:#777;text-align:left;padding:8px 12px}
.select-btn{position:absolute;right:-1px;top:-1px;width:37px;height:36px;background:var(--grey);display:flex;align-items:center;justify-content:center}
.zip-input{position:absolute;left:457px;top:100px;width:111px;height:36px;background:#fff;border:1px solid #ccc}
.search-btn{position:absolute;left:608px;top:100px;width:111px;height:36px;background:var(--dark);color:#fff;font-size:16px;display:flex;align-items:center;justify-content:center;gap:10px}
.search-note{position:absolute;left:0;top:158px;width:100%;font-size:15px;line-height:17px;color:var(--grey)}

.steps-title{position:absolute;top:538px;width:1200px;text-align:center;font-size:30px;font-weight:300;font-style:italic;color:var(--grey)}
.step{position:absolute;top:625px;width:360px;text-align:center;font-size:17px;line-height:17px;color:var(--grey)}
.step svg{display:block;margin:0 auto 35px;height:74px}

.info-box{position:absolute;top:832px;width:528px;height:221px;background:var(--panel);border:1px solid #555}
.info-box h2{text-align:center;margin-top:15px;font-size:27px;font-weight:400;color:var(--grey)}
.person-photo{position:absolute;left:17px;top:58px;width:147px;height:162px;background:linear-gradient(180deg,#f0f0f0 0%,#c9c4bf 40%,#2d2f33 75%,#1f2125 100%)}
.manager-copy{position:absolute;left:182px;top:68px;width:315px;font-size:13.5px;line-height:26px;text-align:justify;color:var(--text)}
.learn-btn{position:absolute;left:182px;top:169px;width:124px;height:39px;background:var(--yellow);border:1px solid #c99b00;border-radius:3px;font-size:17px;color:var(--grey);display:flex;align-items:center;justify-content:center}
.reasons{list-style:none;position:absolute;left:27px;top:76px}
.reasons li{font-size:15px;color:var(--text);margin-bottom:26px;padding-left:33px;position:relative;line-height:18px}
.reasons li svg{position:absolute;left:0;top:5px;width:10px;height:10px}

.site-footer{position:absolute;left:0;top:1100px;width:1200px;height:56px;background:var(--grey);color:#fff;font-size:14px}
.copyright{position:absolute;left:25px;top:19px}
.footer-links{position:absolute;right:23px;top:19px}
</style>
</head>
<body>

<header class="site-header">
  <div class="brand"><span class="brand-mark"></span><span class="brand-name">Venlox</span></div>
  <div class="topbar">
    <span>TALK TO EXPERT</span>
    <svg width="12" height="14" viewBox="0 0 12 14" fill="#4e4c4d"><circle cx="6" cy="4" r="3.5"/><path d="M0 14c0-4 2.5-6 6-6s6 2 6 6z"/></svg>
    <span>800-555-0142</span>
  </div>
  <nav class="main-nav">
    <div class="nav-item"><svg viewBox="0 0 20 20"><path d="M10 2 1 10h3v8h5v-5h2v5h5v-8h3z"/></svg>Home</div>
    <div class="nav-item"><svg viewBox="0 0 20 20"><path d="M10 1a6 6 0 0 0-3.5 10.9V14h7v-2.1A6 6 0 0 0 10 1zm0 2a4 4 0 0 1 2 7.5V12H8v-1.5A4 4 0 0 1 10 3zM7 15h6v2H7zm1 3h4v1H8z"/></svg>Are you a Property Manager?</div>
    <div class="nav-item"><svg viewBox="0 0 20 20"><rect x="1" y="2" width="18" height="17" rx="3"/><path d="M7 6c-1 1-1 3 1 5.5S12 15 13.5 14l1-1-2-1.5-1 .8C10 11.8 8.7 10.5 8.2 9l.8-1L7.5 6z" fill="#fff"/></svg>Contact Us</div>
  </nav>
</header>

<section class="hero" role="img" aria-label="Aerial photo of a neighbourhood of houses with red tiled roofs"></section>

<form class="search-panel">
  <h1>FIND YOUR LOCAL PROPERTY MANAGER</h1>
  <span class="field-label" style="left:32px">Select Your Property Type :</span>
  <span class="field-label" style="left:456px">In Zipcode :</span>
  <div class="select-box">Single Home or Condo ($300 to $500K)
    <span class="select-btn"><svg width="12" height="12" viewBox="0 0 12 12" fill="none" stroke="#fff" stroke-width="2"><path d="M2 1l4 4 4-4M2 6l4 4 4-4"/></svg></span>
  </div>
  <div class="zip-input"></div>
  <div class="search-btn"><svg width="16" height="16" viewBox="0 0 16 16" fill="none" stroke="#fff" stroke-width="2.5"><circle cx="6.5" cy="6.5" r="4.5"/><path d="M10 10l4.5 4.5"/></svg>Search</div>
  <p class="search-note">Search our directory to find experienced and professional property management companies<br>that meet your needs.</p>
</form>

<h2 class="steps-title">To Find Property Management Companies Near You</h2>

<div class="step" style="left:36px">
  <svg viewBox="0 0 80 74" width="80"><path d="M32 2 0 32h8v24h14V40h12v16h10V32h8z" fill="#4e4c4d"/><rect x="40" y="8" width="8" height="14" fill="#4e4c4d"/><rect x="47" y="42" width="30" height="26" rx="3" fill="#fff" stroke="#fbc30a" stroke-width="3"/><path d="M52 54l7 7 16-18" fill="none" stroke="#fbc30a" stroke-width="5"/></svg>
  Select your property type and zipcode
</div>
<div class="step" style="left:417px">
  <svg viewBox="0 0 80 74" width="80"><rect x="0" y="4" width="72" height="56" rx="4" fill="#4e4c4d"/><rect x="6" y="14" width="60" height="40" fill="#fff"/><g fill="#4e4c4d"><rect x="10" y="18" width="4" height="4"/><rect x="18" y="18" width="44" height="4"/><rect x="10" y="26" width="4" height="4"/><rect x="18" y="26" width="44" height="4"/><rect x="10" y="34" width="4" height="4"/><rect x="18" y="34" width="44" height="4"/><rect x="10" y="42" width="4" height="4"/><rect x="18" y="42" width="36" height="4"/></g><circle cx="66" cy="48" r="7" fill="#fbc30a"/><path d="M53 72c0-10 6-14 13-14s13 4 13 14z" fill="#fbc30a"/></svg>
  Review property manager listings in your<br>area
</div>
<div class="step" style="left:798px">
  <svg viewBox="0 0 80 74" width="80"><path d="M8 2h34l14 14v54H8z" fill="#4e4c4d"/><path d="M42 2v14h14" fill="#888"/><g fill="#fff"><rect x="16" y="24" width="28" height="3"/><rect x="16" y="32" width="28" height="3"/><rect x="16" y="40" width="28" height="3"/><rect x="16" y="48" width="20" height="3"/></g><circle cx="54" cy="54" r="5" fill="#fbc30a"/><circle cx="70" cy="50" r="5" fill="#fbc30a"/><circle cx="62" cy="46" r="5" fill="#fbc30a"/><path d="M46 70c0-8 4-11 8-11s8 3 8 11zM62 66c0-8 4-11 8-11s8 3 8 11z" fill="#fbc30a"/></svg>
  Select and compare property managers
</div>

<section class="info-box" style="left:52px">
  <h2>Are you a Property Manager?</h2>
  <div class="person-photo" role="img" aria-label="Portrait photo of a smiling property manager in a suit"></div>
  <p class="manager-copy">Join our real estate property management company network. Let us help you find leads of property owners seeking to rent their homes.</p>
  <div class="learn-btn">Learn More</div>
</section>

<section class="info-box" style="left:620px">
  <h2>What You have to choose Us?</h2>
  <ul class="reasons">
    <li><svg viewBox="0 0 10 10" fill="none" stroke="#4e4c4d" stroke-width="1.5"><path d="M1 1l4 4-4 4M5 1l4 4-4 4"/></svg>Making renting Your home an easy, stress-free experience.</li>
    <li><svg viewBox="0 0 10 10" fill="none" stroke="#4e4c4d" stroke-width="1.5"><path d="M1 1l4 4-4 4M5 1l4 4-4 4"/></svg>Connecting property owners with property managers.</li>
    <li><svg viewBox="0 0 10 10" fill="none" stroke="#4e4c4d" stroke-width="1.5"><path d="M1 1l4 4-4 4M5 1l4 4-4 4"/></svg>Providing property management solutions, simplified.</li>
  </ul>
</section>

<footer class="site-footer">
  <span class="copyright">Copyright © 2014, Venlox, All Rights Reserved</span>
  <span class="footer-links">Are you a Property Manager? &nbsp;|&nbsp; About Us &nbsp;|&nbsp; Contact Us &nbsp;|&nbsp; Terms of Use &nbsp;|&nbsp; Privacy Policy &nbsp;|&nbsp; Site Map</span>
</footer>

</body>
</html>
```